Email Signature

Our company is having its 10th anniversary in 2021. We would like a new email signature to celebrate the occasion. Attached is our business card design.
Please refer to our website for actual contact details.
www.tarvinestates.com.au

Industry/Entity Type

Real Estate

Requirements
Must have
• Our logo
Email
Contact Numbers
Address
Website address

Celebrating 10 years in 2021
Nice to have
• Something that blends the designs of our website and business card

```html
<!DOCTYPE html>
<html lang="en">
<head>
<meta charset="utf-8">
<title>Tarvin Estates – Email Signature</title>
<link rel="stylesheet" href="https://fonts.googleapis.com/css2?family=Poppins:wght@300;400;600&family=Antonio:wght@700&display=swap">
<style>
  :root {
    --page: #d5d5d5;
    --card: #f4f4f4;
    --blue: #1f64ac;
    --ink: #231f20;
    --skyline: #d5dfea;
  }
  * { margin: 0; padding: 0; box-sizing: border-box; }
  html, body { width: 1200px; height: 1200px; overflow: hidden; background: var(--page); }
  .signature {
    position: absolute; left: 127px; top: 491px; width: 946px; height: 218px;
    background: var(--card); overflow: hidden;
    font-family: "Poppins", Arial, sans-serif; color: var(--ink);
  }
  .skyline {
    position: absolute; left: 0; bottom: 0; width: 100%; height: 34px;
    background: linear-gradient(to top, var(--skyline), rgba(213,223,234,0.55));
  }
  .divider { position: absolute; top: 0; width: 1px; height: 100%; background: var(--blue); }
  .divider::after {
    content: ""; position: absolute; left: -2px; top: 39px; width: 5px; height: 142px;
    background: var(--blue); border-radius: 3px;
  }
  .divider--left { left: 313px; }
  .divider--right { left: 636px; }
  .contact { position: absolute; left: 50px; top: 49px; list-style: none; font-size: 13.5px; line-height: 18.8px; }
  .contact li { display: flex; align-items: center; gap: 5px; }
  .contact svg { width: 9px; height: 9px; flex: none; }
  .address { position: absolute; left: 50px; top: 135px; font-size: 13.5px; line-height: 18.8px; }
  .brand {
    position: absolute; left: 314px; width: 322px; top: 136px;
    display: flex; justify-content: center; align-items: center; gap: 8px;
    font-weight: 600; font-size: 26px; color: var(--blue); letter-spacing: 0.5px;
  }
  .brand__dot { width: 12px; height: 12px; border-radius: 50%; background: var(--blue); }
  .anniversary { position: absolute; left: 701px; width: 194px; top: 48px; text-align: center; color: var(--blue); }
  .anniversary__lead { font-family: "Antonio", "Arial Narrow", sans-serif; font-weight: 700; font-size: 46px; line-height: 46px; letter-spacing: 0.3px; }
  .anniversary__years { font-weight: 300; font-size: 37px; line-height: 38px; letter-spacing: 2px; margin-top: -2px; }
  .ribbon { position: absolute; left: 701px; top: 133px; width: 194px; height: 37px; }
  .ribbon__text {
    position: absolute; left: 701px; top: 133px; width: 194px; height: 37px;
    display: flex; align-items: center; justify-content: center;
    font-weight: 600; font-size: 24px; color: #fff;
  }
</style>
</head>
<body>
  <section class="signature">
    <div class="skyline" role="img" aria-label="Faint city skyline silhouette along the bottom edge"></div>

    <ul class="contact">
      <li><svg viewBox="0 0 10 10"><rect x="2.5" y="0.5" width="5" height="9" rx="1" fill="none" stroke="#1f64ac"/><line x1="4" y1="7.8" x2="6" y2="7.8" stroke="#1f64ac"/></svg>555-014-7102</li>
      <li><svg viewBox="0 0 10 10"><path d="M2.5 0.8 L4.2 2.8 L3.3 4 Q4.5 6.5 6.2 7 L7.3 6 L9.2 7.8 L8 9.3 Q3 8.6 1 2 Z" fill="#1f64ac"/></svg>555-019-1909</li>
      <li><svg viewBox="0 0 10 10"><rect x="0.7" y="2" width="8.6" height="6" fill="none" stroke="#1f64ac"/><path d="M0.7 2 L5 5.5 L9.3 2" fill="none" stroke="#1f64ac"/></svg>hello@tarvinestates.com.au</li>
      <li><svg viewBox="0 0 10 10"><circle cx="5" cy="5" r="4.3" fill="none" stroke="#1f64ac" stroke-width="0.8"/><ellipse cx="5" cy="5" rx="1.8" ry="4.3" fill="none" stroke="#1f64ac" stroke-width="0.8"/><line x1="0.7" y1="5" x2="9.3" y2="5" stroke="#1f64ac" stroke-width="0.8"/></svg>www.tarvinestates.com.au</li>
    </ul>

    <p class="address">240 Harbour Street #12<br>Seaview Bay, Florida 33400</p>

    <div class="divider divider--left"></div>

    <div class="brand"><span class="brand__dot"></span>TARVIN ESTATES</div>

    <div class="divider divider--right"></div>

    <div class="anniversary">
      <p class="anniversary__lead">CELEBRATING</p>
      <p class="anniversary__years">10 YEARS</p>
    </div>
    <svg class="ribbon" viewBox="0 0 194 37" aria-hidden="true">
      <polygon points="0,28 20,14 0,0 32,0 28,4 28,28" fill="#1f64ac"/>
      <polygon points="194,28 174,14 194,0 162,0 166,4 166,28" fill="#1f64ac"/>
      <polygon points="28,3 166,3 162,37 32,37" fill="#1f64ac"/>
    </svg>
    <div class="ribbon__text">IN 2021</div>
  </section>
</body>
</html>
```